Contemporary new French wine brand needs logo and series of label design

to design a new contemporary logo and series of labels for a new French wine brand. We hope to attract not just current French wine drinkers but new ones who may appreciate a less traditional and more modern style.
Updates

Reason: we are wanting to extend the project for a few days more to receive more submissions since we had fewer designs submitted than we were expecting, maybe because of the holidays.

Target Market(s)

people who follow the arts community (eg. music, theatre, visual/video arts, dance) --- all mature ages.

Industry/Entity Type

French Wine

Requirements
Must have
• a clear, memorable treatment for the name CLAVINE with accompanying logo.
Nice to have
• embossing, matte/gloss refinement, tasteful foil stamping, coated stock for the whites to help the integrity of the paper in and out of ice buckets. A combo of say, three types of fonts; a semi custom font for the brand name Clavine and maybe a script and one other.
Should not have
• not traditional French

```html
<!DOCTYPE html>
<html lang="fr">
<head>
<meta charset="utf-8">
<title>Clavine — St. Émilion</title>
<link rel="stylesheet" href="https://fonts.googleapis.com/css2?family=Special+Elite&display=swap">
<style>
  :root {
    --sky-top: #c8d6de;
    --sky-bottom: #b3c4cd;
    --sea-top: #728f9b;
    --sea-mid: #56737f;
    --sea-bottom: #3f5863;
    --ink-light: #eef1f1;
    --ink-yellow: #e9d43c;
  }
  * { margin: 0; padding: 0; box-sizing: border-box; }
  html, body {
    width: 1200px;
    height: 1084px;
    overflow: hidden;
    background: var(--sea-mid);
  }
  .label {
    position: relative;
    width: 1200px;
    height: 1084px;
    overflow: hidden;
    font-family: "Special Elite", "Courier New", monospace;
  }
  .label__scene {
    position: absolute;
    inset: 0;
    background: linear-gradient(
      to bottom,
      var(--sky-top) 0%,
      var(--sky-bottom) 28%,
      #9fb2bb 29.5%,
      var(--sea-top) 31%,
      var(--sea-mid) 60%,
      var(--sea-bottom) 100%
    );
  }
  .label__brand {
    position: absolute;
    right: 44px;
    top: 318px;
    font-size: 98px;
    line-height: 1;
    letter-spacing: 26px;
    margin-right: -26px;
    color: var(--ink-light);
    opacity: 0.95;
    white-space: nowrap;
  }
  .label__appellation {
    position: absolute;
    right: 44px;
    top: 420px;
    font-size: 82px;
    line-height: 1;
    letter-spacing: 22px;
    margin-right: -22px;
    color: var(--ink-light);
    opacity: 0.92;
    white-space: nowrap;
  }
  .label__region {
    position: absolute;
    left: 88px;
    top: 962px;
    font-size: 44px;
    line-height: 1;
    letter-spacing: 16px;
    color: var(--ink-yellow);
    white-space: nowrap;
  }
</style>
</head>
<body>
  <main class="label">
    <div class="label__scene" role="img" aria-label="Painterly seascape under a grey sky, a dark headland on the horizon and two yellow buoys floating on choppy water"></div>
    <h1 class="label__brand">CLAVINE</h1>
    <p class="label__appellation">st.émilion</p>
    <p class="label__region">région:bordeaux</p>
  </main>
</body>
</html>
```